Templates for Construction Company

We are looking to have templates prepared for all aspects of our letter sending. Using our brand design. with similar layouts that look the same.

Letterheads design & Email signatures

We use letter heads for - quotes, contract correspondence, variations, formal letters, invitations

Target Market(s)

Clients documents sent in emails

Industry/Entity Type

Construction

Font styles to use
Serif
Sans Serif

Colors
0054AA
0677BA
7BADD7
CADEEF
E8F1F8

Requirements
Must have
• Easy to read, water marks on page
Nice to have
• Different options for different letters

```html
<!DOCTYPE html>
<html lang="en">
<head>
<meta charset="utf-8">
<title>Keystone Construction Group – Letterhead &amp; Email Signature</title>
<link href="https://fonts.googleapis.com/css2?family=Lato:wght@400;700&family=Open+Sans:wght@400;600&display=swap" rel="stylesheet">
<style>
  :root {
    --brand-blue: #5588c8;
    --brand-deep: #0054aa;
    --ink: #3a3a3a;
    --band-grey: #505050;
    --rule: #c8c8c8;
    --paper: #ffffff;
    --backdrop: #e9ebee;
    --watermark: #eef1f5;
  }
  * { margin: 0; padding: 0; box-sizing: border-box; }
  html, body { width: 912px; height: 1200px; overflow: hidden; }
  body { background: var(--backdrop); font-family: "Open Sans", Arial, sans-serif; color: var(--ink); position: relative; }

  .letterhead {
    position: absolute; left: 108px; top: 28px; width: 695px; height: 892px;
    background: var(--paper); box-shadow: 0 2px 10px rgba(0,0,0,.15); overflow: hidden;
  }
  .brand { position: absolute; display: flex; align-items: center; gap: 8px; color: var(--brand-blue); font-family: "Open Sans", Arial, sans-serif; font-weight: 600; }
  .letterhead .brand { left: 68px; top: 40px; font-size: 26px; }
  .brand-mark { width: 22px; height: 22px; background: var(--brand-blue); flex: none; }
  .brand-name small { display: block; font-size: 11px; letter-spacing: .5px; }

  .head-contact { position: absolute; left: 480px; top: 26px; border-left: 1px solid var(--rule); padding-left: 12px; font-size: 13px; line-height: 16.5px; color: var(--ink); }
  .head-contact li { list-style: none; display: flex; align-items: center; gap: 5px; }
  .icon { width: 13px; height: 13px; fill: var(--brand-blue); flex: none; }

  .watermark { position: absolute; left: 295px; top: 290px; width: 106px; height: 300px; background: var(--watermark); }

  .letter-body { position: absolute; left: 66px; top: 161px; width: 562px; font-size: 11px; line-height: 20px; color: var(--ink); }
  .letter-body .meta { line-height: 13.5px; margin-bottom: 12px; }
  .letter-body p { margin-bottom: 20px; text-align: justify; }
  .salutation { margin: 32px 0 20px; }
  .sign-off { margin-top: 30px; }
  .signature-sample { display: block; width: 160px; height: 18px; margin: 10px 0 8px; background: linear-gradient(90deg, #d9d9d9, #ececec); border-radius: 9px; }
  .signer-name { font-size: 14px; line-height: 18px; }
  .signer-role { font-size: 11px; line-height: 24px; }

  .footer-rule { position: absolute; left: 0; right: 0; top: 794px; height: 4px; background: var(--band-grey); }
  .footer-band { position: absolute; left: 0; right: 0; top: 804px; bottom: 0; background: var(--brand-blue); }
  .footer-address { position: absolute; right: 71px; top: 827px; text-align: right; color: #fff; font-family: Arial, sans-serif; font-size: 13px; line-height: 16px; font-style: normal; }

  .email-signature {
    position: absolute; left: 138px; top: 958px; width: 635px; height: 190px;
    background: var(--paper); box-shadow: 0 2px 10px rgba(0,0,0,.15); font-family: "Lato", Arial, sans-serif;
  }
  .email-signature .brand { left: 26px; top: 50px; font-size: 24px; }
  .social { position: absolute; left: 53px; top: 140px; display: flex; gap: 6px; }
  .social span { width: 22px; height: 22px; border-radius: 50%; background: var(--brand-blue); }
  .sig-name { position: absolute; left: 226px; top: 22px; font-size: 21px; line-height: 22px; color: var(--brand-blue); }
  .sig-role { position: absolute; left: 226px; top: 44px; font-size: 16px; color: var(--ink); }
  .sig-rule { position: absolute; left: 226px; right: 0; top: 74px; border-top: 1px solid var(--rule); }
  .sig-contact { position: absolute; left: 226px; top: 94px; font-size: 15.5px; line-height: 20px; color: var(--ink); }
  .sig-contact li { list-style: none; display: flex; align-items: center; gap: 6px; }
  .sig-contact li + li.address { margin-top: 14px; }
  .sig-contact .icon { width: 15px; height: 15px; }
</style>
</head>
<body>
<svg width="0" height="0" style="position:absolute">
  <symbol id="i-phone" viewBox="0 0 16 16"><path d="M2 5c0-2 2-3 6-3s6 1 6 3v1h-3V4.5H5V6H2zM4 7h8l2 6H2z"/></symbol>
  <symbol id="i-mobile" viewBox="0 0 16 16"><path d="M4 1h8v14H4zM5.5 2.5v10h5v-10z"/></symbol>
  <symbol id="i-mail" viewBox="0 0 16 16"><path d="M1 3h14v10H1zM2.5 4.5 8 9l5.5-4.5z"/></symbol>
  <symbol id="i-globe" viewBox="0 0 16 16"><circle cx="8" cy="8" r="7"/></symbol>
  <symbol id="i-pin" viewBox="0 0 16 16"><path d="M8 1a5 5 0 0 1 5 5c0 4-5 9-5 9S3 10 3 6a5 5 0 0 1 5-5zm0 3a2 2 0 1 0 0 4 2 2 0 0 0 0-4z"/></symbol>
</svg>

<main class="letterhead">
  <div class="brand"><span class="brand-mark"></span><span class="brand-name">Keystone<small>CONSTRUCTION GROUP</small></span></div>

  <ul class="head-contact">
    <li><svg class="icon"><use href="#i-phone"/></svg>044-555 010 247</li>
    <li><svg class="icon"><use href="#i-mail"/></svg>info@keystonebuild.net</li>
    <li><svg class="icon"><use href="#i-globe"/></svg>www.keystonebuild.net</li>
  </ul>

  <div class="watermark" aria-hidden="true"></div>

  <section class="letter-body">
    <div class="meta">Issuing Date: May 5, 2018</div>
    <div class="meta">Name Of Employee Mr. XYZABC<br>Address of Employee<br>Address Line 2 etc..</div>
    <div class="salutation">Dear Mr.XYZABC</div>
    <p>Lorem Ipsum has been the industry's standard dummy text ever since the 1500s, when an unknown printer took a galley of type and scrambled it to make a type specimen book. It has survived not only five centuries, but also the leap into electronic typesetting, remaining essentially unchanged. It was popularised in the 1960s with the release of transfer sheets containing Lorem Ipsum passages, and more recently with desktop layout software including versions of Lorem Ipsum.</p>
    <p>Lorem Ipsum is simply dummy text of the printing and typesetting industry. Lorem Ipsum has been the industry's standard dummy text ever since the 1500s, when an unknown printer took a galley of type and scrambled it to make a type specimen book.</p>
    <p>It has survived not only five centuries, but also the leap into electronic typesetting, remaining essentially unchanged. It was popularised in the 1960s with the release of transfer sheets containing Lorem Ipsum passages.</p>
    <div class="sign-off">Yours Sincerely</div>
    <span class="signature-sample" role="img" aria-label="Handwritten signature of Daniel Carter"></span>
    <div class="signer-name">Daniel Carter</div>
    <div class="signer-role">Managing Director</div>
  </section>

  <div class="footer-rule" aria-hidden="true"></div>
  <div class="footer-band" aria-hidden="true"></div>
  <address class="footer-address">87 Harbour Road<br>30418, Westland</address>
</main>

<section class="email-signature">
  <div class="brand"><span class="brand-mark"></span><span class="brand-name">Keystone<small>CONSTRUCTION GROUP</small></span></div>
  <div class="social" aria-label="Social links"><span></span><span></span><span></span></div>
  <div class="sig-name">Daniel Carter</div>
  <div class="sig-role">Managing Director</div>
  <div class="sig-rule"></div>
  <ul class="sig-contact">
    <li><svg class="icon"><use href="#i-mobile"/></svg>044-555 010 247 <svg class="icon"><use href="#i-phone"/></svg>044-555 010 247</li>
    <li><svg class="icon"><use href="#i-mail"/></svg>info@keystonebuild.net <svg class="icon"><use href="#i-globe"/></svg>www.keystonebuild.net</li>
    <li class="address"><svg class="icon"><use href="#i-pin"/></svg>87 Harbour Road, 30418, Westland</li>
  </ul>
</section>
</body>
</html>
```